What does your organisation do?
TALVO
We need a website for our business – A Holding Company

Objective:
1. User-friendly design and navigation
2. Content management
3. Language (English and Arabic)
4. Download PDF or scan for profile

Navigations and Sub-Navigations:
1. Profile
a. About Us
b. Vision-Mission
c. Corporate Governance
d. Sustainability
2. Business Sector
a. Food
b. Logistics
c. Retail
d. Trading and Distribution
e. Government Services
3. Investor Relations
4. Careers
5. Contact Us
Footer:
Contact Us
1. Address
2. Contact Number
3. Email Address
4. Social Media (LinkedIn Logo)
Company / Quick Links
• About Us
• Vision & Mission
• Careers

Newsletter
Get the latest information from us and our group companies. Be amongst the first to know and stay updated on the go. Join our mailing list
Email Text Box with Subscribe button.

Competitors / Reference:
URL 1: https://www.quirenholding.example/
URL 2: https://www.mibelholding.example/
URL 3: https://vzp.example

Target Market(s)

Individual and customer businesses customers

Industry/Entity Type

Financial

Coding

Coded - Design and coding required

Number of Pages Required

5+ page

Font styles to use
Serif
Sans Serif

Requirements
Must have

• 1. SEO Friendly website ( Meta tags, description, title, proper keywords)
2. Ability to make modifications easily in future. (Provide front end for adding content, images etc.)
3. Chatbot Widget with enquiry form – integration with google sheet
4. Register website with Google (Google Search Console)
5. Register website with Google My Business
Nice to have
• See uploaded file for reference

```html
<!DOCTYPE html>
<html lang="en">
<head>
<meta charset="utf-8">
<title>TALVO Holding – Diversified Investments in Food, Logistics, Retail and Trading</title>
<meta name="description" content="TALVO is a holding company with businesses in food, logistics, retail, trading and distribution, and government services.">
<meta name="keywords" content="TALVO, holding company, investments, logistics, food, retail, trading, government services">
<link href="https://fonts.googleapis.com/css2?family=Montserrat:ital,wght@0,400;0,500;0,600;0,700;1,400&family=Noto+Kufi+Arabic:wght@600&display=swap" rel="stylesheet">
<style>
:root{
  --sky:#1fb4ea;
  --sky-bright:#29b6f6;
  --navy:#1b2a45;
  --navy-deep:#15223a;
  --ink:#2b2f3a;
  --text:#4a4f5a;
  --muted:#777d88;
  --pale:#f0f8fd;
  --white:#ffffff;
  --line:#dde3ea;
}
*{margin:0;padding:0;box-sizing:border-box}
html,body{width:1200px;height:3504px;overflow:hidden}
body{position:relative;font-family:"Montserrat",Arial,sans-serif;color:var(--text);background:var(--white)}
.abs{position:absolute}

/* hero */
.hero{left:0;top:0;width:1200px;height:700px;background:linear-gradient(180deg,#4c6a86 0%,#b98a6f 28%,#7f8b92 48%,#6d7478 62%,#8a7a4c 80%,#6f6436 100%)}
.nav-rule{left:0;top:70px;width:1200px;height:1px;background:rgba(255,255,255,.35)}
.brand{font-weight:700;color:var(--white);letter-spacing:1px}
.nav a{position:absolute;top:27px;font-size:12.5px;font-weight:600;color:var(--white);text-decoration:none;letter-spacing:.3px;white-space:nowrap}
.nav .lang{top:21px;font-family:"Noto Kufi Arabic",sans-serif;font-size:13px;border:1px solid rgba(255,255,255,.7);padding:2px 12px;border-radius:3px}
.nav-active{left:430px;top:66px;width:60px;height:3px;background:var(--sky)}
.hero-panel{left:106px;top:299px;width:411px;height:222px;background:var(--sky);opacity:.95}
.hero-title{left:147px;top:340px;font-size:27px;font-weight:700;color:var(--white);white-space:nowrap}
.hero-sub{left:147px;top:382px;font-size:18px;color:var(--white);line-height:21px}
.btn-quote{left:146px;top:442px;width:149px;height:38px;border:2px solid var(--white);color:var(--white);font-size:13px;font-weight:700;display:flex;align-items:center;justify-content:center}
.dot{width:8px;height:8px;border-radius:50%;background:var(--white)}
.dot.ring{width:14px;height:14px;background:none;border:2px solid var(--white)}

.sec-title{font-size:33px;font-weight:600;color:var(--ink);letter-spacing:.5px}
.bar{height:3px;background:var(--sky)}

/* sectors */
.card{top:834px;width:300px;height:420px;border:1px solid var(--line);background:var(--white);text-align:center}
.card.dark{background:var(--navy);border-color:var(--navy)}
.card-photo{position:absolute;left:0;top:0;width:100%;height:203px}
.card-icon{position:absolute;left:109px;top:162px;width:82px;height:82px;border-radius:50%;background:var(--sky);border:4px solid var(--white)}
.card h3{position:absolute;left:0;top:258px;width:100%;font-size:18px;font-weight:600;color:var(--ink)}
.card.dark h3,.card.dark p{color:var(--white)}
.card .mini{position:absolute;left:130px;top:290px;width:40px;height:3px;background:var(--sky)}
.card p{position:absolute;left:30px;top:304px;width:240px;font-size:11.5px;line-height:17.5px;color:var(--muted)}

.special{left:0;top:1347px;width:1200px;height:547px;background:var(--pale)}
.h-sub{font-size:23px;font-weight:600;color:var(--ink)}
.para{font-size:15px;line-height:27px;color:var(--ink)}

.pro-list{left:654px;top:2070px;width:540px;list-style:none}
.pro-list li{position:relative;padding-left:29px;font-size:11.5px;letter-spacing:-.1px;line-height:16px;color:var(--text);margin-bottom:9.5px}
.pro-list li svg{position:absolute;left:0;top:0}

.testi{left:0;top:2494px;width:1200px;height:483px;background:linear-gradient(90deg,#c8bcb4 0%,#d9cfc8 35%,#e6d8c9 50%,#aeb79d 70%,#8f9f7a 100%)}
.quote-card{left:147px;top:2623px;width:423px;height:256px;background:var(--white);border-radius:4px;box-shadow:0 6px 20px rgba(0,0,0,.12);text-align:center}

.partner{top:3018px;height:30px;background:#c5c9cf;border-radius:4px}

.footer{left:0;top:3090px;width:1200px;height:349px;background:var(--navy)}
.footer-base{left:0;top:3439px;width:1200px;height:65px;background:var(--navy-deep)}
.f-head{font-size:13px;font-weight:700;color:var(--white)}
.f-rule{height:1px;background:var(--sky)}
.f-link{font-size:11.5px;color:var(--white)}
.f-q{font-size:11.5px;font-weight:600;color:var(--white)}
.f-a{font-size:9.5px;color:#c7cfdc}
.social{top:3303px;width:30px;height:30px;border-radius:50%;border:2px solid var(--white)}
.social.first{background:var(--sky);border-color:var(--sky)}
.news-input{left:610px;top:3286px;width:190px;height:34px;border:1px solid #4a5a78;background:var(--navy-deep);color:#9aa6ba;font-size:10.5px;padding:0 10px;display:flex;align-items:center}
.news-btn{left:800px;top:3286px;width:74px;height:34px;background:var(--sky);color:var(--white);font-size:10.5px;font-weight:700;display:flex;align-items:center;justify-content:center}
</style>
</head>
<body>

<section class="abs hero" role="img" aria-label="Photo of a freight truck on a highway at sunset, representing the group's logistics business"></section>
<div class="abs nav-rule"></div>
<div class="abs brand" style="left:133px;top:14px;font-size:36px">TALVO</div>
<nav class="nav">
  <a style="left:433px">PROFILE</a>
  <a style="left:527px">BUSINESS SECTOR</a>
  <a style="left:668px">INVESTOR RELATIONS</a>
  <a style="left:831px">CAREERS</a>
  <a style="left:921px">CONTACT US</a>
  <a class="lang" lang="ar" style="left:1030px">العربية</a>
</nav>
<div class="abs nav-active"></div>
<div class="abs hero-panel"></div>
<h1 class="abs hero-title">INVESTING IN GROWTH</h1>
<p class="abs hero-sub">A diversified holding company<br>building lasting value.</p>
<div class="abs btn-quote">OUR PROFILE</div>
<div class="abs dot" style="left:550px;top:669px"></div>
<div class="abs dot ring" style="left:569px;top:666px"></div>
<div class="abs dot" style="left:594px;top:669px"></div>

<h2 class="abs sec-title" style="left:0;width:1200px;text-align:center;top:750px">BUSINESS SECTORS</h2>
<div class="abs bar" style="left:561px;top:795px;width:78px"></div>

<article class="abs card" style="left:129px">
  <div class="card-photo" role="img" aria-label="Photo of fresh food products in production" style="background:linear-gradient(135deg,#cfd6dc,#8a9aa8)"></div>
  <div class="card-icon"></div>
  <h3>Food</h3><div class="mini"></div>
  <p>Our food companies source, produce and supply quality products to homes, restaurants and retailers across the region, with strict standards at every step.</p>
</article>
<article class="abs card dark" style="left:452px">
  <div class="card-photo" role="img" aria-label="Illustration of a world map with shipping routes" style="background:linear-gradient(135deg,#2a86c8,#1c6aa8)"></div>
  <div class="card-icon"></div>
  <h3>Logistics</h3><div class="mini"></div>
  <p>Land, sea and air networks that move goods for businesses and individuals, from same-day local delivery to international freight and warehousing.</p>
</article>
<article class="abs card" style="left:769px">
  <div class="card-photo" role="img" aria-label="Illustration of retail and online shopping" style="background:linear-gradient(180deg,#1f4f6a,#163d55)"></div>
  <div class="card-icon"></div>
  <h3>Retail, Trading &amp; Distribution</h3><div class="mini"></div>
  <p>Retail outlets and trading arms that distribute trusted brands to customers, with supply chains managed through modern technology.</p>
</article>

<section class="abs special"></section>
<h2 class="abs sec-title" style="left:135px;top:1464px;font-size:30px">OUR PROFILE</h2>
<div class="abs bar" style="left:135px;top:1509px;width:77px"></div>
<h3 class="abs h-sub" style="left:135px;top:1549px">VISION &amp; MISSION</h3>
<p class="abs para" style="left:135px;top:1592px;width:470px">Our vision is to be a trusted group that creates value for our customers, partners and investors.</p>
<p class="abs para" style="left:135px;top:1665px;width:470px">We do this through sound corporate governance, long-term sustainability and businesses that serve the community.</p>
<div class="abs" role="img" aria-label="Illustration of the group's leadership and regional presence on a map" style="left:619px;top:1415px;width:531px;height:479px;background:linear-gradient(135deg,#c9c3e3 0%,#b4aed8 45%,#e8f2fa 100%);border-radius:6px"></div>

<div class="abs" role="img" aria-label="Illustration of a representative handing documents to a client" style="left:92px;top:1973px;width:508px;height:390px;background:linear-gradient(160deg,#d6ecfa 0%,#b5def6 60%,#e9f6fd 100%);border-radius:40px"></div>
<h2 class="abs h-sub" style="left:650px;top:1982px">GOVERNMENT SERVICES</h2>
<h3 class="abs" style="left:650px;top:2025px;font-size:18.5px;font-weight:600;color:var(--sky-bright)">Dedicated PRO services include:</h3>
<ul class="abs pro-list">
  <li><svg width="16" height="16" viewBox="0 0 16 16"><circle cx="8" cy="8" r="8" fill="#1fb4ea"/><path d="M6.5 4.5 10 8l-3.5 3.5" stroke="#fff" stroke-width="2" fill="none"/></svg>Processing, renewal and cancellation of visas</li>
  <li><svg width="16" height="16" viewBox="0 0 16 16"><circle cx="8" cy="8" r="8" fill="#1fb4ea"/><path d="M6.5 4.5 10 8l-3.5 3.5" stroke="#fff" stroke-width="2" fill="none"/></svg>Registration of companies with Ministry of Labor and Department of Immigration</li>
  <li><svg width="16" height="16" viewBox="0 0 16 16"><circle cx="8" cy="8" r="8" fill="#1fb4ea"/><path d="M6.5 4.5 10 8l-3.5 3.5" stroke="#fff" stroke-width="2" fill="none"/></svg>Amendment or renewal of company labor and immigration cards</li>
  <li><svg width="16" height="16" viewBox="0 0 16 16"><circle cx="8" cy="8" r="8" fill="#1fb4ea"/><path d="M6.5 4.5 10 8l-3.5 3.5" stroke="#fff" stroke-width="2" fill="none"/></svg>Renewal and amendment (address change) of trade licenses</li>
  <li><svg width="16" height="16" viewBox="0 0 16 16"><circle cx="8" cy="8" r="8" fill="#1fb4ea"/><path d="M6.5 4.5 10 8l-3.5 3.5" stroke="#fff" stroke-width="2" fill="none"/></svg>VIP services for medicals</li>
  <li><svg width="16" height="16" viewBox="0 0 16 16"><circle cx="8" cy="8" r="8" fill="#1fb4ea"/><path d="M6.5 4.5 10 8l-3.5 3.5" stroke="#fff" stroke-width="2" fill="none"/></svg>Visa deposits at airport and VIP arrival service</li>
  <li><svg width="16" height="16" viewBox="0 0 16 16"><circle cx="8" cy="8" r="8" fill="#1fb4ea"/><path d="M6.5 4.5 10 8l-3.5 3.5" stroke="#fff" stroke-width="2" fill="none"/></svg>Stamping certificates from the Ministry of Foreign Affairs</li>
  <li><svg width="16" height="16" viewBox="0 0 16 16"><circle cx="8" cy="8" r="8" fill="#1fb4ea"/><path d="M6.5 4.5 10 8l-3.5 3.5" stroke="#fff" stroke-width="2" fill="none"/></svg>Extension of visit visas</li>
  <li><svg width="16" height="16" viewBox="0 0 16 16"><circle cx="8" cy="8" r="8" fill="#1fb4ea"/><path d="M6.5 4.5 10 8l-3.5 3.5" stroke="#fff" stroke-width="2" fill="none"/></svg>Application for refunds of bank guarantees by Ministry of Labor and deposits made at Department of Immigration</li>
  <li><svg width="16" height="16" viewBox="0 0 16 16"><circle cx="8" cy="8" r="8" fill="#1fb4ea"/><path d="M6.5 4.5 10 8l-3.5 3.5" stroke="#fff" stroke-width="2" fill="none"/></svg>Emirates ID card form completion</li>
</ul>

<section class="abs testi" role="img" aria-label="Photo of a satisfied customer and a company representative outdoors"></section>
<h2 class="abs" style="left:147px;top:2557px;width:423px;text-align:center;font-size:28px;font-weight:600;color:var(--white)">TESTIMONIALS</h2>
<div class="abs" style="left:323px;top:2601px;width:72px;height:2px;background:var(--white)"></div>
<div class="abs quote-card">
  <svg class="abs" style="left:188px;top:29px" width="48" height="48" viewBox="0 0 48 48"><circle cx="24" cy="24" r="22.5" fill="none" stroke="#1fb4ea" stroke-width="2"/><path d="M15 28c0-5 2-8 6-10M24 28c0-5 2-8 6-10" stroke="#1fb4ea" stroke-width="2.5" fill="none" stroke-linecap="round"/><circle cx="18" cy="28" r="3" fill="#1fb4ea"/><circle cx="27" cy="28" r="3" fill="#1fb4ea"/></svg>
  <p class="abs" style="left:42px;top:90px;width:340px;font-size:13px;line-height:21.5px;font-style:italic;color:var(--muted)">Lorem ipsum dolor sit amet, consectetur adipiscing elit, sed do eiusmod tempor incididunt ut labore et dolore magna aliqua. Ut enim ad minim veniam, quis nostrud exercitationpsum dolor sit amet</p>
  <p class="abs" style="left:0;top:190px;width:423px;font-size:12.5px;font-weight:600;color:var(--ink)">MARA ELLISON</p>
  <p class="abs" style="left:0;top:211px;width:423px;font-size:11px;color:var(--muted)">Founder, Norvel Company</p>
</div>
<div class="abs dot" style="left:346px;top:2905px;width:7px;height:7px"></div>
<div class="abs dot ring" style="left:362px;top:2902px;width:13px;height:13px"></div>
<div class="abs dot" style="left:385px;top:2905px;width:7px;height:7px"></div>

<div class="abs partner" style="left:135px;width:106px"></div>
<div class="abs partner" style="left:351px;width:82px"></div>
<div class="abs partner" style="left:543px;width:112px"></div>
<div class="abs partner" style="left:762px;width:86px"></div>
<div class="abs partner" style="left:957px;width:108px"></div>

<footer class="abs footer"></footer>
<div class="abs brand" style="left:158px;top:3166px;font-size:36px">TALVO</div>
<p class="abs" style="left:158px;top:3232px;width:210px;font-size:11.5px;line-height:17px;color:var(--white)">A diversified holding company investing in businesses that serve customers every day.</p>
<div class="abs social first" style="left:152px" aria-label="LinkedIn"></div>

<div class="abs f-head" style="left:423px;top:3167px">COMPANY</div>
<div class="abs f-rule" style="left:423px;top:3190px;width:129px"></div>
<div class="abs f-link" style="left:426px;top:3225px">About Us</div>
<div class="abs f-link" style="left:426px;top:3253px">Vision &amp; Mission</div>
<div class="abs f-link" style="left:426px;top:3282px">Careers</div>
<div class="abs f-link" style="left:426px;top:3310px">Investor Relations</div>
<div class="abs f-link" style="left:426px;top:3339px">Profile (PDF)</div>

<div class="abs f-head" style="left:610px;top:3167px">NEWSLETTER</div>
<div class="abs f-rule" style="left:610px;top:3190px;width:126px"></div>
<p class="abs f-a" style="left:610px;top:3216px;width:264px;font-size:10px;line-height:15px">Get the latest information from us and our group companies. Be amongst the first to know and stay updated on the go. Join our mailing list.</p>
<div class="abs news-input">Your email address</div>
<div class="abs news-btn">SUBSCRIBE</div>

<div class="abs f-head" style="left:911px;top:3167px">CONTACT US</div>
<div class="abs f-rule" style="left:911px;top:3190px;width:131px"></div>
<svg class="abs" style="left:913px;top:3212px" width="28" height="28" viewBox="0 0 32 32"><circle cx="16" cy="16" r="16" fill="#1fb4ea"/><path d="M16 8a5 5 0 0 0-5 5c0 4 5 10 5 10s5-6 5-10a5 5 0 0 0-5-5z" fill="#fff"/><circle cx="16" cy="13" r="2" fill="#1fb4ea"/></svg>
<div class="abs f-a" style="left:950px;top:3214px;font-size:10.5px;line-height:14px;color:var(--white)">22 Harlow Lane, N7 2QD<br>London, United Kingdom</div>
<svg class="abs" style="left:913px;top:3256px" width="28" height="28" viewBox="0 0 32 32"><circle cx="16" cy="16" r="16" fill="#1fb4ea"/><path d="M11 9l3 0 1.5 4-2 1.5a9 9 0 0 0 4 4l1.5-2 4 1.5 0 3a2 2 0 0 1-2 2A13 13 0 0 1 9 11a2 2 0 0 1 2-2z" fill="#fff"/></svg>
<div class="abs f-a" style="left:950px;top:3264px;font-size:11px;color:var(--white)">+1 555-014-2290</div>
<svg class="abs" style="left:913px;top:3300px" width="28" height="28" viewBox="0 0 32 32"><circle cx="16" cy="16" r="16" fill="#1fb4ea"/><rect x="9" y="11" width="14" height="10" rx="1" fill="#fff"/><path d="M9.5 11.5 16 17l6.5-5.5" stroke="#1fb4ea" stroke-width="1.5" fill="none"/></svg>
<div class="abs f-a" style="left:950px;top:3308px;font-size:11px;color:var(--white)">info@talvo.example</div>

<div class="abs footer-base"></div>
<div class="abs f-a" style="left:167px;top:3461px;font-size:10px;color:var(--white)">Copyright © 2012-2020 TALVO. All rights reserved</div>
<div class="abs f-a" style="left:921px;top:3461px;font-size:10px;color:var(--white)">Privacy</div>
<div class="abs f-a" style="left:976px;top:3461px;font-size:10px;color:var(--white)">Terms &amp; Use</div>
<div class="abs f-a" style="left:1050px;top:3461px;font-size:10px;color:var(--white)">Sitemap</div>

</body>
</html>
```